Sunny Paths and joy Business card

I have a logo, but will like a business card design. Is for a travel agency in Mexico. We focus in family experiences.

I will liek some thing different and unique, from the traditional business card, something to get remmeber for.

Business card information:

Leandro T. Ocampo
leandro@sunnypathsjoy.example

Alameda 482, 3 piso
Col. Tlalpizco
Mexico, D.F. 07320

office: (55) 5000-0142
mobile: (55) 9000-0187

www.sunnypathsjoy.example
@sunnypjoy
blog: sunnypathsandjoy.blogsite.example
facebook: SunnyPathsAndJoy

```html
<!DOCTYPE html>
<html lang="es">
<head>
<meta charset="utf-8">
<title>Sunny Paths and joy — Business card</title>
<link rel="stylesheet" href="https://fonts.googleapis.com/css2?family=Source+Sans+3:wght@400;600;700&display=swap">
<style>
  :root {
    --paper: #ffffff;
    --ink-name: #1e5aa8;
    --ink-contact: #2a66c9;
    --ink-address: #3b82da;
    --ink-brand: #1d4f9f;
    --sky-soft: #d3eff9;
    --band: #a9e0f4;
  }
  * { margin: 0; padding: 0; box-sizing: border-box; }
  html, body { width: 1200px; height: 705px; overflow: hidden; background: var(--paper); }
  .card {
    position: relative;
    width: 1200px; height: 705px;
    background: var(--paper);
    font-family: "Source Sans 3", sans-serif;
  }
  .brand-halo {
    position: absolute;
    left: 205px; top: 108px;
    width: 300px; height: 300px;
    border-radius: 50%;
    background: var(--sky-soft);
  }
  .brand-name {
    position: absolute;
    left: 42px; top: 282px;
    width: 510px;
    text-align: center;
    font-weight: 700;
    font-size: 74px;
    line-height: 0.98;
    color: var(--ink-brand);
  }
  .person {
    position: absolute;
    left: 560px; top: 247px;
    width: 560px;
    text-align: center;
  }
  .person-name {
    font-weight: 700;
    font-size: 34px;
    line-height: 43px;
    color: var(--ink-name);
  }
  .person-line {
    font-size: 30px;
    line-height: 43px;
    color: var(--ink-contact);
  }
  .address {
    position: absolute;
    left: 62px; top: 511px;
    font-size: 30px;
    line-height: 43px;
    font-style: normal;
    color: var(--ink-address);
    font-variant-numeric: oldstyle-nums;
  }
  .online {
    position: absolute;
    left: 622px; top: 496px;
    font-size: 25px;
    line-height: 36px;
    color: var(--ink-address);
  }
  .band {
    position: absolute;
    left: 0; width: 1200px; height: 8px;
    background: var(--band);
  }
  .band-top { top: 641px; }
  .band-bottom { top: 655px; }
</style>
</head>
<body>
  <main class="card">
    <div class="brand-halo" role="img" aria-label="Sunny Paths and joy brand emblem area"></div>
    <div class="brand-name">Sunny Paths<br>and joy</div>

    <section class="person">
      <p class="person-name">Leandro T. Ocampo</p>
      <p class="person-line">leandro@sunnypathsjoy.example</p>
      <p class="person-line">office: (55) 5000-0142</p>
      <p class="person-line">mobile: (55) 9000-0187</p>
    </section>

    <address class="address">
      Alameda 482, 3 piso<br>
      Col. Tlalpizco<br>
      Mexico, D.F. 07320
    </address>

    <section class="online">
      <p>www.sunnypathsjoy.example</p>
      <p>@sunnypjoy</p>
      <p>blog: sunnypathsandjoy.blogsite.example</p>
      <p>facebook: SunnyPathsAndJoy</p>
    </section>

    <div class="band band-top"></div>
    <div class="band band-bottom"></div>
  </main>
</body>
</html>
```